Dermatopathology Brochure

We need a brochure that will let potential clients know our services. It needs to be clean, clear, and eye-catching. A modern feel is what we would like. Some previous work done for us in the past has been included. We have uploaded a word file with content as well. You may also use information from our website, veltramorisclinic.com. You don't have to use all available information, but the content of the word file is our main message.
Updates

Although the postcard highlights our Qorvi based online clinicopathologic correlation, we would like our brochure to be more general. In other words, we use postcards to make a single important point, but the brochure should be more balanced regarding our services. Also, the postcard was great for us, but we don't necessarily want to repeat its look exactly. We liked the postacard's clean and balanced look. We would like to try having our brochure more "friendly" and conversational, yet professional. Thanks!

Target Market(s)

Physicians, mostly dermatologists.

Industry/Entity Type

Work

```html
<!DOCTYPE html>
<html lang="en">
<head>
<meta charset="utf-8">
<title>Dermatopathology Brochure</title>
<link href="https://fonts.googleapis.com/css2?family=Source+Sans+3:wght@400;600;700&display=swap" rel="stylesheet">
<style>
  :root {
    --red: #e4222b;
    --red-deep: #c8283a;
    --tissue-pink: #e0677a;
    --tissue-rose: #d9485e;
    --sidebar: #383232;
    --band: #3a3838;
    --slide-black: #060606;
    --white: #ffffff;
    --text-light: #fbe9ea;
  }
  * { margin: 0; padding: 0; box-sizing: border-box; }
  html, body { width: 1200px; height: 849px; overflow: hidden; background: var(--band); }
  body { font-family: "Source Sans 3", "Source Sans Pro", sans-serif; color: var(--white); }

  .brochure { position: relative; width: 1200px; height: 849px; overflow: hidden; }

  .tissue-backdrop {
    position: absolute; left: 0; top: 0; width: 1200px; height: 647px;
    background:
      radial-gradient(ellipse 520px 260px at 900px 520px, rgba(170,40,70,0.55), transparent 70%),
      radial-gradient(ellipse 600px 200px at 560px 470px, rgba(240,120,130,0.35), transparent 70%),
      linear-gradient(180deg, var(--red) 0%, var(--red) 38%, var(--tissue-rose) 62%, var(--tissue-pink) 80%, var(--red-deep) 100%);
  }

  .profile {
    position: absolute; left: 30px; top: 0; width: 240px; height: 647px;
    background: var(--sidebar); text-align: center;
  }
  .profile-photo {
    position: absolute; left: 38px; top: 62px; width: 165px; height: 163px;
    border: 4px solid var(--red);
    background: linear-gradient(180deg, #c9c0a8 0%, #a9a08c 55%, #2a2a33 100%);
  }
  .profile-name { position: absolute; left: 0; top: 241px; width: 240px; font-weight: 700; font-size: 17.5px; line-height: 22px; }
  .profile-bio { position: absolute; left: 8px; top: 263px; width: 224px; font-size: 17.5px; line-height: 22px; }

  .column { position: absolute; top: 56px; }
  .column h2 { font-size: 32px; font-weight: 700; line-height: 36px; letter-spacing: 0.2px; }
  .column .tagline { font-size: 16px; font-weight: 700; line-height: 21.5px; margin-top: 4px; }
  .column .body { font-size: 16px; line-height: 21.6px; margin-top: 20px; color: var(--text-light); }

  .col-expertise { left: 330px; width: 270px; }
  .col-availability { left: 660px; width: 230px; }
  .col-connectivity { left: 930px; width: 220px; }

  .contact { position: absolute; left: 330px; font-size: 16px; line-height: 21.6px; color: var(--text-light); }
  .contact strong { color: var(--white); font-weight: 700; display: block; }
  .contact-mail { top: 497px; }
  .contact-phone { top: 583px; }
  .website { position: absolute; left: 660px; top: 601px; font-size: 16px; font-weight: 700; }

  .slide-strip { position: absolute; left: 0; top: 647px; width: 1200px; height: 202px; background: var(--band); }
  .slide-strip svg { position: absolute; left: 12px; top: 11px; }
</style>
</head>
<body>
<main class="brochure">
  <div class="tissue-backdrop" role="img" aria-label="Magnified skin tissue section in red and pink tones"></div>

  <aside class="profile">
    <div class="profile-photo" role="img" aria-label="Portrait photograph of the dermatopathologist"></div>
    <p class="profile-name">Adrian L. Pell, M.D.</p>
    <p class="profile-bio">Dr. Pell graduated from Harwick Medical College and completed his Internal Medicine internship at the Westmere Valley program. He completed his Dermatology residency, and subsequently his Dermatopathology Fellowship, at Brantley College of Medicine in Eastport. Dr. Pell is board-certified in Dermatology and Dermatopathology.</p>
  </aside>

  <section class="column col-expertise">
    <h2>Expertise</h2>
    <p class="tagline">academic teaching<br>hospitals to private practice.</p>
    <p class="body">Dr. Pell has worked as<br>a consultant dermatopathologist for the University of Solano, Ardmore Department of Dermatology, interpreting challenging cases from the teaching hospital floors and academic dermatologist offices.<br>He has, and continues<br>to provide interpretations for dermatologists in typical private practice as well.</p>
  </section>

  <section class="column col-availability">
    <h2>Availability</h2>
    <p class="tagline">we're here for you and<br>your patients.</p>
    <p class="body">We believe the flow of information between treating physician and consultant dermatopathologist is vital for high quality patient care. That's why whether on the phone or using 21st Century communication technology, such as web-based clinicopathologic conferencing, we want to hear what you have to say.</p>
  </section>

  <section class="column col-connectivity">
    <h2>Connectivity</h2>
    <p class="tagline">saving your valuable<br>staff time.</p>
    <p class="body">Depending on your medical record system, we can mail, fax, or directly upload reports into your electronic medical records.&nbsp; Paper or electronic, we'll try to make your workflow easier.</p>
  </section>

  <p class="contact contact-mail"><strong>Mailing address</strong>4120 E. Linden Ave. #210,<br>Harborview, CA 90000</p>
  <p class="contact contact-phone"><strong>Telephone</strong>800.555.0172</p>
  <p class="website">www.veltramorisclinic.com</p>

  <div class="slide-strip">
    <svg width="1176" height="178" viewBox="0 0 1176 178" role="img" aria-label="Three microscope views of stained skin tissue">
      <defs>
        <clipPath id="strip-clip"><rect width="1176" height="178"/></clipPath>
        <radialGradient id="slide-a" cx="50%" cy="45%" r="60%"><stop offset="0" stop-color="#d58a9e"/><stop offset="1" stop-color="#a2547a"/></radialGradient>
        <radialGradient id="slide-b" cx="50%" cy="50%" r="60%"><stop offset="0" stop-color="#c06a9a"/><stop offset="1" stop-color="#9d5b86"/></radialGradient>
        <radialGradient id="slide-c" cx="50%" cy="50%" r="60%"><stop offset="0" stop-color="#e0a0b0"/><stop offset="1" stop-color="#b86a8a"/></radialGradient>
      </defs>
      <rect width="1176" height="178" fill="var(--slide-black)"/>
      <g clip-path="url(#strip-clip)">
        <circle cx="208" cy="88" r="160" fill="url(#slide-a)"/>
        <circle cx="628" cy="88" r="160" fill="url(#slide-b)"/>
        <circle cx="1022" cy="88" r="160" fill="url(#slide-c)"/>
      </g>
    </svg>
  </div>
</main>
</body>
</html>
```